Velmorique needs a elegant mystical business card design

The theme of Velmorique is centered on Kemetic/Ancient Egyptian Spirituality. My business sells handmade scented candles, mystic oils, body sprays, tarot readings and more. I would like my business card to reflect an elegant and mystical look. Hieroglyphs around the borders would be a cool idea. Also, the main colors I am working with is Black and Gold= colors of royalty. Black background. The business card will be double sided. The back will have the logo, and the front will have the basic information (ie name, title, business, phone, email, website, etc..)

Target Market(s)

The target market are people into metaphysics, holistic healing, ancient Egyptian culture, aromatherapy, occult science, and the esoteric.

Industry/Entity Type

Business

Contact Information for Business Card

Name: Marlonda T. Pruitt
Title: Owner
Business: VELMORIQUE
Phone: 917.302.4417
Website: www.Velmorique.net
Facebook, Instagram, and twitter icons

Font styles to use
Serif
Decorative

Requirements
Must have
• My logo, and website.
Nice to have
• Ancient Egyptian hieroglyphs, Elegant designs around the border, or encircling the logo.

```html
<!DOCTYPE html>
<html lang="en">
<head>
<meta charset="utf-8">
<title>Velmorique Business Card</title>
<link rel="stylesheet" href="https://fonts.googleapis.com/css2?family=Cinzel:wght@500&family=Tinos:wght@400;700&display=swap">
<style>
  :root {
    --page: #e9e4dc;
    --ink: #060606;
    --gold: #c9a86a;
    --gold-deep: #9b7a42;
    --stone-light: #eab077;
    --stone-mid: #d08a4a;
    --stone-dark: #a35c25;
    --rule: rgba(90, 45, 15, .55);
    --rule-light: rgba(255, 220, 170, .35);
    --white: #f4f1ea;
  }
  * { margin: 0; padding: 0; box-sizing: border-box; }
  html, body { width: 1200px; height: 909px; overflow: hidden; background: var(--page); }
  .canvas { position: relative; width: 1200px; height: 909px; }
  .card {
    position: absolute; top: 300px; width: 540px; height: 309px;
    overflow: hidden; box-shadow: 0 8px 24px rgba(0,0,0,.25);
  }
  .card--back { left: 40px; }
  .card--front { left: 620px; background: var(--ink); }

  .stone-panel {
    position: relative; width: 100%; height: 100%;
    background: radial-gradient(ellipse at 45% 40%, var(--stone-light) 0%, var(--stone-mid) 55%, var(--stone-dark) 100%);
  }
  .stone-panel__rules {
    position: absolute; inset: 0;
    background: repeating-linear-gradient(
      to bottom,
      transparent 0 34px,
      var(--rule) 34px 36px,
      var(--rule-light) 36px 37px
    );
  }
  .stone-panel__bands {
    position: absolute; inset: 0;
    background: repeating-linear-gradient(
      to bottom,
      rgba(120, 60, 20, .10) 0 6px,
      transparent 6px 30px,
      rgba(120, 60, 20, .10) 30px 37px
    );
  }

  .brand {
    position: absolute; left: 170px; top: 72px; width: 310px;
    display: flex; align-items: center; justify-content: center; gap: 12px;
    font-family: "Cinzel", serif; font-weight: 500; font-size: 27px;
    letter-spacing: 5px; color: var(--gold);
  }
  .brand__dot { width: 10px; height: 10px; border-radius: 50%; background: var(--gold); flex: none; }

  .person { position: absolute; left: 28px; top: 130px; }
  .person__name {
    font-family: "Tinos", serif; font-size: 32px; color: var(--gold); line-height: 1;
  }
  .person__title {
    font-family: "Tinos", serif; font-weight: 700; font-size: 24px; color: var(--white);
    line-height: 1; margin-top: 4px;
  }
  .divider { position: absolute; left: 272px; top: 182px; width: 2px; height: 64px; background: var(--white); }
  .contacts {
    position: absolute; left: 292px; top: 186px; list-style: none;
    font-family: "Tinos", serif; font-size: 19px; color: var(--white);
  }
  .contacts li { display: flex; align-items: center; gap: 14px; height: 28px; }
  .contacts svg { width: 14px; height: 14px; flex: none; }
  .footer-wave { position: absolute; left: 0; bottom: 0; width: 540px; height: 76px; }
</style>
</head>
<body>
<main class="canvas">
  <section class="card card--back">
    <div class="stone-panel" role="img" aria-label="Rows of carved ancient Egyptian hieroglyphs on warm sandstone">
      <div class="stone-panel__bands"></div>
      <div class="stone-panel__rules"></div>
    </div>
  </section>

  <section class="card card--front">
    <div class="brand"><span class="brand__dot"></span><span>VELMORIQUE</span></div>

    <div class="person">
      <div class="person__name">Marlonda T. Pruitt</div>
      <div class="person__title">Owner</div>
    </div>

    <div class="divider"></div>

    <ul class="contacts">
      <li>
        <svg viewBox="0 0 14 14"><rect width="14" height="14" rx="2" fill="#f4f1ea"/><path d="M4 3.5c-.8.5-1 1.6.2 3.4s2.6 3 3.6 3.2c.8.1 1.6-.4 1.9-.9l-1.4-1.2-.9.6c-.7-.3-1.6-1.2-2-2l.5-.9L4.8 3.3z" fill="#060606"/></svg>
        <span>917.302.4417</span>
      </li>
      <li>
        <svg viewBox="0 0 14 14"><rect width="14" height="14" rx="2" fill="#f4f1ea"/><circle cx="7" cy="7" r="4.2" fill="none" stroke="#060606" stroke-width="1.2"/><path d="M2.8 7h8.4M7 2.8c-1.6 2.5-1.6 5.9 0 8.4M7 2.8c1.6 2.5 1.6 5.9 0 8.4" fill="none" stroke="#060606" stroke-width=".9"/></svg>
        <span>www.Velmorique.net</span>
      </li>
    </ul>

    <svg class="footer-wave" viewBox="0 0 540 76" preserveAspectRatio="none" role="img" aria-label="Strip of carved hieroglyphs beneath a gold curve">
      <defs>
        <linearGradient id="stoneBand" x1="0" y1="0" x2="1" y2="0">
          <stop offset="0" stop-color="#b8733a"/>
          <stop offset=".5" stop-color="#dc9a5a"/>
          <stop offset="1" stop-color="#b06c33"/>
        </linearGradient>
        <clipPath id="bandClip">
          <path d="M0 8 C180 14 380 40 540 76 L0 76 Z"/>
        </clipPath>
      </defs>
      <path d="M0 8 C180 14 380 40 540 76 L0 76 Z" fill="url(#stoneBand)"/>
      <g clip-path="url(#bandClip)" stroke="rgba(90,45,15,.5)" stroke-width="1">
        <line x1="0" y1="30" x2="540" y2="30"/>
        <line x1="0" y1="52" x2="540" y2="52"/>
        <line x1="0" y1="72" x2="540" y2="72"/>
      </g>
      <path d="M0 0 C180 6 400 32 540 68 L540 76 C380 40 180 14 0 8 Z" fill="#060606"/>
      <path d="M60 3 C230 10 420 40 540 66" fill="none" stroke="#c9a86a" stroke-width="3"/>
    </svg>
  </section>
</main>
</body>
</html>
```